Boutique custom software development company needs new business card

Our nearly 20 year old custom software development company would like to better include the fact that we are now providing Bitcoin services. These new services are B2B include education (how to acquire and securely hold Bitcoin) and integrating Bitcoin payments into existing ecommerce sites or other existing systems. Please keep the card clean and simple. Attached is our current design and some other files. vexalon.example

Target Market(s)

businesses owners interested in long term relationship

Industry/Entity Type

Custom software development and Bitcoin

Contact Information for Business Card

Marcus Ellwood, marcus@vexalon.example, vexalon.example, (888) 555-VEXAL

Font styles to use
Other font styles liked:
• monospace

Requirements
Must have
• double-sided
Nice to have
• clean and simple
Should not have
• physical address

```html
<!DOCTYPE html>
<html lang="en">
<head>
<meta charset="utf-8">
<title>Vexalon business card</title>
<link rel="stylesheet" href="https://fonts.googleapis.com/css2?family=Open+Sans:ital,wght@0,400;0,700;1,400&display=swap">
<style>
  :root {
    --backdrop: #c4c4c4;
    --paper: #f8f8f7;
    --brand-blue: #3b70b8;
    --brand-blue-deep: #1f4f93;
    --brand-blue-light: #6f9ee0;
    --accent-orange: #ee7424;
    --edge-orange: #d65a12;
    --ink: #1c1c1c;
    --rule: #bdbdbd;
  }
  * { box-sizing: border-box; margin: 0; padding: 0; }
  html, body { width: 695px; height: 1200px; overflow: hidden; }
  body {
    background: var(--backdrop);
    font-family: "Open Sans", Arial, sans-serif;
    position: relative;
  }
  .card {
    position: absolute;
    left: 47px;
    width: 600px;
    height: 343px;
    border-bottom: 3px solid var(--edge-orange);
    box-shadow: 0 14px 28px rgba(0,0,0,0.25);
    overflow: hidden;
  }
  .card--front { top: 190px; background: var(--paper); }
  .card--back { top: 650px; background: var(--brand-blue); }

  .front__brand {
    position: absolute;
    left: 58px;
    top: 134px;
    width: 240px;
  }
  .brand-name {
    font-weight: 700;
    font-size: 40px;
    letter-spacing: 1px;
    line-height: 1;
    color: var(--brand-blue);
  }
  .brand-tagline {
    margin-top: 6px;
    font-size: 12.5px;
    font-style: italic;
    color: var(--brand-blue);
  }
  .front__divider {
    position: absolute;
    left: 312px;
    top: 70px;
    width: 1px;
    height: 200px;
    background: var(--rule);
  }
  .contact {
    position: absolute;
    left: 336px;
    top: 72px;
    color: var(--ink);
    font-size: 13px;
    line-height: 1.35;
  }
  .contact__name {
    font-weight: 700;
    font-size: 19px;
    color: var(--brand-blue);
    margin-bottom: 8px;
  }
  .contact__services { margin-bottom: 12px; }
  .contact__list { list-style: none; }
  .contact__item { display: flex; align-items: center; gap: 7px; }
  .contact__icon { width: 10px; height: 10px; flex: none; }

  .back__field {
    position: absolute;
    right: 0;
    top: 0;
    width: 340px;
    height: 100%;
    background: linear-gradient(135deg, var(--brand-blue-deep) 0%, var(--brand-blue) 55%, var(--brand-blue-light) 100%);
    clip-path: polygon(22% 0, 100% 0, 100% 100%, 0 100%);
  }
  .back__brand {
    position: absolute;
    left: 0;
    width: 100%;
    top: 146px;
    display: flex;
    justify-content: center;
    align-items: center;
    gap: 10px;
  }
  .back__mark {
    width: 22px;
    height: 22px;
    background: var(--accent-orange);
  }
  .back__name {
    font-weight: 700;
    font-size: 40px;
    letter-spacing: 1px;
    color: #ffffff;
    line-height: 1;
  }
</style>
</head>
<body>
  <section class="card card--front" aria-label="Card front">
    <div class="front__brand">
      <div class="brand-name">VEXALON</div>
      <div class="brand-tagline">developer of custom applications</div>
    </div>
    <div class="front__divider"></div>
    <div class="contact">
      <div class="contact__name">Marcus Ellwood</div>
      <div class="contact__services">Custom software development<br>Bitcoin education &amp; custody<br>Bitcoin payment integration</div>
      <ul class="contact__list">
        <li class="contact__item">
          <svg class="contact__icon" viewBox="0 0 10 10"><path d="M2 1 L4 1 L4.6 3 L3.4 3.8 Q4.5 6 6.2 6.6 L7 5.4 L9 6 L9 8 Q8.5 9 7.5 9 Q1 8 1 2.5 Q1 1.5 2 1Z" fill="var(--accent-orange)"/></svg>
          (888) 555-VEXAL
        </li>
        <li class="contact__item">
          <svg class="contact__icon" viewBox="0 0 10 10"><rect x="2.5" y="0.5" width="5" height="9" rx="1" fill="none" stroke="var(--accent-orange)" stroke-width="1.2"/><circle cx="5" cy="7.8" r="0.6" fill="var(--accent-orange)"/></svg>
          502.555.0148
        </li>
        <li class="contact__item">
          <svg class="contact__icon" viewBox="0 0 10 10"><rect x="0.5" y="2" width="9" height="6" fill="var(--accent-orange)"/><path d="M0.5 2 L5 5.5 L9.5 2" fill="none" stroke="#fff" stroke-width="0.9"/></svg>
          marcus@vexalon.example
        </li>
        <li class="contact__item">
          <svg class="contact__icon" viewBox="0 0 10 10"><circle cx="5" cy="5" r="4.3" fill="none" stroke="var(--accent-orange)" stroke-width="1"/><ellipse cx="5" cy="5" rx="1.8" ry="4.3" fill="none" stroke="var(--accent-orange)" stroke-width="0.8"/><line x1="0.7" y1="5" x2="9.3" y2="5" stroke="var(--accent-orange)" stroke-width="0.8"/></svg>
          www.vexalon.example
        </li>
      </ul>
    </div>
  </section>

  <section class="card card--back" aria-label="Card back">
    <div class="back__field" role="img" aria-label="Large faint brand decoration in layered blue tones"></div>
    <div class="back__brand">
      <span class="back__mark"></span>
      <span class="back__name">VEXALON</span>
    </div>
  </section>
</body>
</html>
```